Dear Designer
I am looking for some proposal for the graphic design of our new web site
www.drelvox.com; you can find in real time the developper version on : drelvox.tabrino.info/?id=308

We do not need web page programing... no IT stuff .. only to provide me graphic contents for some pages:
- home
- contact us
- product page
- download page
- blog page
- application page
Pls advise me back asap
Thank you
Henrik

```html
<!DOCTYPE html>
<html lang="en">
<head>
<meta charset="utf-8">
<title>Drelvox Power Transmission</title>
<link href="https://fonts.googleapis.com/css2?family=Montserrat:wght@400;500;600;700;800&family=Open+Sans:wght@400;600&family=Varela+Round&display=swap" rel="stylesheet">
<style>
:root{
  --blue:#0a6abf;
  --blue-dark:#0857a3;
  --blue-light:#2e8fe0;
  --grey:#b3b8bd;
  --grey-band:#c4c8cc;
  --text:#555b61;
  --title:#2b2f33;
  --white:#ffffff;
  --line:#e4e6e8;
}
*{margin:0;padding:0;box-sizing:border-box}
html,body{width:1200px;height:3873px;overflow:hidden}
body{position:relative;background:var(--white);font-family:'Open Sans',sans-serif;color:var(--text)}
.abs{position:absolute}
.center{left:0;width:1200px;text-align:center}

/* top bar */
.topbar{top:0;left:0;width:1200px;height:50px;background:var(--blue)}
.topbar .slant{position:absolute;top:0;right:0;width:400px;height:50px;background:var(--grey);clip-path:polygon(20px 0,100% 0,100% 100%,0 100%)}
.topbar .info{position:absolute;top:0;height:50px;display:flex;align-items:center;gap:9px;color:var(--white);font-family:'Montserrat',sans-serif;font-size:16px}

/* header */
.header{top:50px;left:0;width:1200px;height:138px;background:var(--white)}
.brand{position:absolute;left:112px;top:28px;font-family:'Montserrat',sans-serif;color:var(--blue);font-weight:800}
.brand .name{font-size:58px;line-height:58px;letter-spacing:1px;display:block}
.brand .tag{font-size:17px;font-weight:800;letter-spacing:.5px;display:block;margin-top:4px}
.nav{position:absolute;top:64px;left:0;width:1200px;font-family:'Montserrat',sans-serif;font-size:15px;font-weight:500;color:#333}
.nav span{position:absolute;top:0}
.nav .active{color:var(--blue)}

/* hero */
.hero{top:188px;left:0;width:1200px;height:702px;background:linear-gradient(180deg,#5d86c4 0%,#3f74c0 30%,#5a7ec2 55%,#2f72b8 80%,#1b5fa8 100%)}
.hero .glow{position:absolute;inset:0;background:radial-gradient(circle at 10% 68%,rgba(230,120,180,.55),transparent 35%),radial-gradient(circle at 85% 45%,rgba(120,220,255,.35),transparent 40%)}
.hero h1{position:absolute;left:0;width:1200px;text-align:center;color:var(--white);font-family:'Montserrat',sans-serif;font-weight:700}
.hero .t1{top:440px;font-size:100px;line-height:110px;letter-spacing:3px}
.hero .t2{top:568px;font-size:58px;line-height:66px;font-weight:600}
.btn-main{position:absolute;left:510px;top:659px;width:180px;height:57px;background:var(--blue);color:var(--white);font-family:'Montserrat',sans-serif;font-weight:600;font-size:18px;display:flex;align-items:center;justify-content:center;border-radius:2px}

/* section headings */
.sec-title{font-family:'Varela Round',sans-serif;font-size:40px;color:var(--blue);line-height:48px}
.sec-sub{font-size:15.5px;line-height:29px;color:var(--text)}

/* product cards */
.card{position:absolute;top:1113px;width:233px;height:328px;background:var(--white);box-shadow:0 0 8px rgba(0,0,0,.12);text-align:center}
.card .pic{position:absolute;left:20px;top:15px;width:193px;height:143px;background:radial-gradient(ellipse at center,#3a3d40 0%,#6b6f73 45%,#f2f3f4 75%)}
.card h3{position:absolute;top:170px;width:100%;font-family:'Montserrat',sans-serif;font-weight:500;font-size:19px;color:#333}
.card p{position:absolute;top:205px;left:20px;width:193px;font-size:13px;line-height:24px}
.card .more{position:absolute;left:58px;top:267px;width:117px;height:35px;border:1.5px solid var(--blue);color:var(--blue);font-family:'Montserrat',sans-serif;font-size:12.5px;font-weight:500;display:flex;align-items:center;justify-content:center}

/* applications */
.apps{top:1525px;left:0;width:1200px;height:644px;background:linear-gradient(180deg,#1f78d0 0%,#2b86d8 40%,#2a7fd0 75%,#1a64b2 100%)}
.apps .white{color:var(--white)}
.tile{position:absolute;width:181px;height:151px;border:2px solid rgba(255,255,255,.85);border-radius:4px;background:rgba(255,255,255,.08);color:var(--white);text-align:center;font-family:'Montserrat',sans-serif;font-size:15px;font-weight:500;line-height:20px}
.tile svg{position:absolute;left:55px;top:18px;width:70px;height:70px;fill:none;stroke:var(--white);stroke-width:3;stroke-linejoin:round;stroke-linecap:round}
.tile span{position:absolute;left:0;width:100%;top:99px}

/* blog */
.post{position:absolute;top:2357px;width:313px;height:425px;background:var(--white);box-shadow:0 0 8px rgba(0,0,0,.12)}
.post .pic{position:absolute;left:0;top:0;width:313px;height:224px}
.post .date{position:absolute;top:15px;right:22px;width:72px;height:72px;border-radius:50%;background:var(--blue);color:var(--white);font-family:'Montserrat',sans-serif;text-align:center;font-weight:500}
.post .date b{display:block;font-size:21px;font-weight:500;margin-top:13px;line-height:22px}
.post .date i{display:block;font-style:normal;font-size:14px;line-height:18px}
.post h3{position:absolute;top:248px;left:18px;width:280px;font-family:'Montserrat',sans-serif;font-weight:600;font-size:21px;line-height:31px;color:var(--title)}
.post p{position:absolute;top:318px;left:21px;width:280px;font-size:13.5px;line-height:25px;color:#777}

/* story */
.story{top:2870px;left:0;width:1200px;height:502px;background:var(--grey-band)}
.story .photo{position:absolute;left:0;top:0;width:1200px;height:502px;background:linear-gradient(160deg,#3a78c9 0%,#5d95d4 45%,#8fb5df 100%);clip-path:polygon(0 0,629px 0,560px 100%,0 100%)}
.story h2{position:absolute;left:677px;top:2934px;font-family:'Varela Round',sans-serif;font-weight:400;font-size:40px;color:var(--white)}
.story-text{position:absolute;left:677px;width:414px;color:var(--white);font-size:15.5px;line-height:24px}

/* contact */
.contact-brand{position:absolute;left:208px;top:3590px;width:330px;text-align:center;font-family:'Montserrat',sans-serif;font-weight:800;color:var(--blue)}
.contact-brand .name{display:block;font-size:84px;line-height:86px;letter-spacing:1px}
.contact-brand .tag{display:block;font-size:25px;line-height:30px;margin-top:4px}
.divider{position:absolute;left:610px;top:3552px;width:1px;height:184px;background:#ccc}
.ci{position:absolute;left:681px;width:460px;height:44px}
.ci .ring{position:absolute;left:0;top:0;width:42px;height:42px;border:2px solid var(--blue);border-radius:50%;display:flex;align-items:center;justify-content:center}
.ci .ring svg{width:16px;height:16px;fill:var(--blue)}
.ci .lab{position:absolute;left:57px;top:1px;font-family:'Montserrat',sans-serif;font-size:13.5px;color:#555;line-height:18px}
.ci .val{position:absolute;left:57px;top:23px;font-family:'Montserrat',sans-serif;font-size:11.5px;color:#444;line-height:16px}

/* footer */
.footer{top:3790px;left:0;width:1200px;height:83px;background:var(--blue)}
.footer .slant{position:absolute;top:0;right:0;width:460px;height:83px;background:var(--grey);clip-path:polygon(42px 0,100% 0,100% 100%,0 100%)}
.footer .copy{position:absolute;left:111px;top:32px;color:var(--white);font-size:15px}
.social{position:absolute;top:22px;width:40px;height:40px;border:2px solid var(--white);border-radius:50%}
</style>
</head>
<body>

<!-- top bar -->
<div class="abs topbar">
  <div class="slant"></div>
  <div class="info" style="left:110px">
    <svg width="11" height="15" viewBox="0 0 12 16"><path d="M6 0C2.7 0 0 2.6 0 5.9 0 10.3 6 16 6 16s6-5.7 6-10.1C12 2.6 9.3 0 6 0zm0 8.2a2.3 2.3 0 1 1 0-4.6 2.3 2.3 0 0 1 0 4.6z" fill="#fff"/></svg>
    14, rue des Ateliers 38200 Vienne France
  </div>
  <div class="info" style="left:850px">
    <svg width="14" height="14" viewBox="0 0 16 16"><path d="M3.6 1l2.3 3.3-1.4 1.7c.9 2 2.5 3.6 4.5 4.5l1.7-1.4L14 11.4 12.8 14C6.4 14 2 9.6 2 3.2z" fill="#fff"/></svg>
    Call Us : +33 612 45 80 37
  </div>
</div>

<!-- header -->
<div class="abs header">
  <div class="brand"><span class="name">DRELVOX</span><span class="tag">POWER TRANSMISSION</span></div>
  <nav class="nav">
    <span class="active" style="left:421px">HOME</span>
    <span style="left:510px">PRODUCT</span>
    <span style="left:626px">DOWNLOAD</span>
    <span style="left:763px">BLOG</span>
    <span style="left:847px">APPLICATION</span>
    <span style="left:991px">CONTACT US</span>
  </nav>
</div>

<!-- hero -->
<section class="abs hero" role="img" aria-label="Electricity pylons under a cloudy sky with a glowing network overlay">
  <div class="glow"></div>
</section>
<div class="hero abs" style="background:none">
  <h1 class="t1">DRELVOX</h1>
  <h1 class="t2">POWER TRANSMISSION</h1>
  <div class="btn-main">READ MORE</div>
</div>

<!-- products -->
<h2 class="abs center sec-title" style="top:953px;font-weight:400">Our Products</h2>
<p class="abs center sec-sub" style="top:1012px">Drelvox Power Transmission is a major manufacturer of power transmission<br>systems for specific applications.</p>

<div class="card" style="left:111px">
  <div class="pic" role="img" aria-label="Ribbed belt product photo"></div>
  <h3>Ribbed Belts</h3>
  <p>We use it to encourage ideas will change the world</p>
  <div class="more">VIEW DETAILS</div>
</div>
<div class="card" style="left:359px">
  <div class="pic" role="img" aria-label="Timing belts with pulleys product photo"></div>
  <h3>Timing Belts</h3>
  <p>We use it to encourage ideas will change the world</p>
  <div class="more">VIEW DETAILS</div>
</div>
<div class="card" style="left:608px">
  <div class="pic" role="img" aria-label="V-belt product photo" style="background:radial-gradient(ellipse at center,#2f3d2f 0%,#5d6a5d 40%,#f2f3f4 72%)"></div>
  <h3>V-Belts</h3>
  <p>We use it to encourage ideas will change the world</p>
  <div class="more">VIEW DETAILS</div>
</div>
<div class="card" style="left:856px">
  <div class="pic" role="img" aria-label="Agricultural belt product photo"></div>
  <h3>Agri-Belts</h3>
  <p>We use it to encourage ideas will change the world</p>
  <div class="more">VIEW DETAILS</div>
</div>

<!-- applications -->
<section class="abs apps" role="img" aria-label="Blue-tinted landscape with power line towers"></section>
<h2 class="abs center sec-title" style="top:1575px;color:#fff;font-weight:400">Applications</h2>
<p class="abs center sec-sub" style="top:1634px;color:#fff">Drelvox Power Transmission is a major manufacturer of power transmission<br>systems for specific applications.</p>

<div class="tile" style="left:112px;top:1730px">
  <svg viewBox="0 0 70 70"><circle cx="18" cy="50" r="10"/><circle cx="54" cy="54" r="6"/><path d="M10 40V14h22l6 22h18v14"/><path d="M28 50h20"/><path d="M40 36V22"/></svg>
  <span>AGRICULTURE</span>
</div>
<div class="tile" style="left:311px;top:1730px">
  <svg viewBox="0 0 70 70"><rect x="14" y="4" width="42" height="62" rx="3"/><path d="M14 16h42"/><circle cx="35" cy="40" r="14"/><circle cx="35" cy="40" r="8"/></svg>
  <span>APPLIANCES<br>MACHINERY</span>
</div>
<div class="tile" style="left:510px;top:1730px">
  <svg viewBox="0 0 70 70"><circle cx="24" cy="48" r="12"/><path d="M10 64h50M44 64V30l10-20M24 48l16-14M20 28h14"/></svg>
  <span>FITNESS</span>
</div>
<div class="tile" style="left:708px;top:1730px">
  <svg viewBox="0 0 70 70"><path d="M6 14l22 26h30v14H22z"/><circle cx="26" cy="58" r="6"/><circle cx="54" cy="58" r="6"/><path d="M44 20c4-10 14-10 18-8-2 8-10 12-18 8z"/></svg>
  <span>GARDENING<br>LAWN MOWER</span>
</div>
<div class="tile" style="left:907px;top:1730px">
  <svg viewBox="0 0 70 70"><path d="M10 48a25 25 0 0 1 50 0z"/><path d="M4 54h62"/><circle cx="35" cy="18" r="4"/></svg>
  <span>FOOD &amp; BEVERAGE</span>
</div>

<div class="tile" style="left:112px;top:1913px">
  <svg viewBox="0 0 70 70"><path d="M8 8h8l12 44"/><circle cx="30" cy="58" r="6"/><rect x="22" y="16" width="26" height="30" transform="rotate(-15 35 31)"/></svg>
  <span>LOGISTIC<br>MOVEMENT</span>
</div>
<div class="tile" style="left:311px;top:1913px">
  <svg viewBox="0 0 70 70"><path d="M4 22h40l-4 20H8z"/><path d="M44 28h14l8 12v10H4v-8"/><circle cx="16" cy="52" r="7"/><circle cx="32" cy="52" r="7"/><circle cx="54" cy="52" r="7"/></svg>
  <span>MINING &amp;<br>QUARRYING</span>
</div>
<div class="tile" style="left:510px;top:1913px">
  <svg viewBox="0 0 70 70"><path d="M35 10l24 12v26L35 60 11 48V22z"/><path d="M11 22l24 12 24-12M35 34v26"/></svg>
  <span>PACKAGING</span>
</div>
<div class="tile" style="left:708px;top:1913px">
  <svg viewBox="0 0 70 70"><path d="M14 12h38l4 48H18z"/><path d="M14 12c-6 6-6 12 0 18M56 22c6 6 6 12 0 18"/></svg>
  <span>PULP &amp; PAPER</span>
</div>
<div class="tile" style="left:907px;top:1913px">
  <svg viewBox="0 0 70 70"><path d="M28 10l10 0 8 14M50 20l-4 4-6-2"/><path d="M14 32L8 44l6 10h14M8 36l6-4 4 6"/><path d="M62 44l-6 10H42M56 56l-4-2 2-6"/></svg>
  <span>RECYCLING</span>
</div>

<!-- blog -->
<h2 class="abs center sec-title" style="top:2214px;font-weight:400">Latest Blog</h2>
<p class="abs center sec-sub" style="top:2272px">Drelvox Power Transmission is a major manufacturer of power transmission<br>systems for specific applications.</p>

<article class="post" style="left:111px">
  <div class="pic" role="img" aria-label="Close-up of steel gears in a gearbox" style="background:linear-gradient(135deg,#9aa0a6,#5a6066 50%,#c2c6ca)"></div>
  <div class="date"><b>10</b><i>APR</i></div>
  <h3>Lorem Ipsum is simply the dummy text</h3>
  <p>It is a long established fact that a reader will be distracted by the readable content page when looking at its layout.</p>
</article>
<article class="post" style="left:444px">
  <div class="pic" role="img" aria-label="Power line tower against an orange sunset" style="background:linear-gradient(180deg,#4a6b9a 0%,#c98a4a 55%,#f0a030 80%,#5a3a1a 100%)"></div>
  <div class="date"><b>10</b><i>APR</i></div>
  <h3>Lorem Ipsum is simply the dummy text</h3>
  <p>It is a long established fact that a reader will be distracted by the readable content page when looking at its layout.</p>
</article>
<article class="post" style="left:776px">
  <div class="pic" role="img" aria-label="Hands holding an industrial gear on a dark workbench" style="background:linear-gradient(135deg,#2a2c2e,#5b5e62 50%,#3a3c3e)"></div>
  <div class="date"><b>10</b><i>APR</i></div>
  <h3>Lorem Ipsum is simply the dummy text</h3>
  <p>It is a long established fact that a reader will be distracted by the readable content page when looking at its layout.</p>
</article>

<!-- story -->
<section class="abs story">
  <div class="photo" role="img" aria-label="Two engineers in hard hats inspecting power line towers"></div>
</section>
<div class="story">
  <h2>Our Story</h2>
  <p class="story-text" style="top:3006px">Drelvox Power Transmission is a major manufacturer of power transmission systems for specific applications. At Drelvox PT, we aim to push the limits of materials science in order to create products that consistently surpass expectations.</p>
  <p class="story-text" style="top:3150px">We don't take for granted our long history of development. We use it to encourage ideas that will change world in the coming decades. We invest in R&amp;D and technology on a regular basis to ensure that our products not only meet industry requirements, but also surpass our customers' expectations.</p>
</div>

<!-- contact -->
<h2 class="abs center sec-title" style="top:3414px;font-weight:400">Contact Us</h2>
<p class="abs center sec-sub" style="top:3472px">Drelvox Power Transmission is a major manufacturer of power transmission<br>systems for specific applications.</p>

<div class="contact-brand"><span class="name" style="font-size:62px">DRELVOX</span><span class="tag">POWER TRANSMISSION</span></div>
<div class="divider"></div>

<div class="ci" style="top:3561px">
  <div class="ring"><svg viewBox="0 0 12 16"><path d="M6 0C2.7 0 0 2.6 0 5.9 0 10.3 6 16 6 16s6-5.7 6-10.1C12 2.6 9.3 0 6 0zm0 8.2a2.3 2.3 0 1 1 0-4.6 2.3 2.3 0 0 1 0 4.6z"/></svg></div>
  <div class="lab">ADDRESS</div>
  <div class="val">14, rue des Ateliers 38200 Vienne France</div>
</div>
<div class="ci" style="top:3626px">
  <div class="ring"><svg viewBox="0 0 16 16"><path d="M3.6 1l2.3 3.3-1.4 1.7c.9 2 2.5 3.6 4.5 4.5l1.7-1.4L14 11.4 12.8 14C6.4 14 2 9.6 2 3.2z"/></svg></div>
  <div class="lab">PHONE</div>
  <div class="val">+33 612 45 80 37</div>
</div>
<div class="ci" style="top:3692px">
  <div class="ring"><svg viewBox="0 0 16 16"><path d="M1 3h14v10H1z M1 3l7 6 7-6" fill="none" stroke="#0a6abf" stroke-width="1.8"/></svg></div>
  <div class="lab">EMAIL US</div>
  <div class="val">management@drelvox.com</div>
</div>

<!-- footer -->
<footer class="abs footer">
  <div class="slant"></div>
  <div class="copy">Copyright ©2021. All rights reserved. &nbsp;|&nbsp; Privacy Policy</div>
  <div class="social" style="left:836px"></div>
  <div class="social" style="left:885px"></div>
  <div class="social" style="left:934px"></div>
  <div class="social" style="left:982px"></div>
</footer>

</body>
</html>
```